Website for Sports and Exercise Medicine Doctor with active research in stem cells therapies.

I am a sports and exercise medicine doctor with research interests in the cutting edge areas of biological therapies, most notable stem cells. None of my patients are dying of anything, and most of them come to see me to decrease their pain, so they can get back to what they want to do.

The approach i then take is to decrease their pain and support them to achieve the things they wish to achieve. Most people start at "Just make it stop hurting doc" , but I try to move them towards something more important over time.

I would like the website to be very different to other "Doctor or medical websites" in its look. No pictures of doctors in white coats and no pictures of fit old people smiling. I would potentially like the fist thing seen to be a quote:

"Less pain. Everybody wants it, but what are you going to do, once you've got it?"

(But this is only an idea, I am open to anything)

The website will need a couple of things

1. "Locations" I work
2. "Research" I am involved in
3. "Sort Me out" - Clinical information for people to access
4. "Social" - imbedded twitter and facebook
5. "Blog" - imbedded wordpress blog
6. "Bio" - the usual bio-stuff

The "Sort Me out" - pages I would like to have the functionality as seen in this site http://www.veltarion.com.au/platelet/. I intend to put disease topics into these pages (eg Achilles tehdinopathy, osteoarthritis etc etc etc). Once again I am not wedded to this but something along these lines would be good.

To give you an idea these are some sites I like
http://www.morbanquilt.com/
http://daptrine.com/
http://ovimbera.com.sg/
http://jolvaniketchup.com/
http://www.pilnorwave.com/
http://quadrisel.com/#offering
http://fennikstudio.tv/
http://norvalgate.com/
http://sablethorn.co.uk/#about

Target Market(s)

20-80 year old.
People with tendon injuries
People with osteoarthritis
People interested in stem cells
I will build the site over time to contain information on multiple sporting injuries and musculoskeletal disorders. It will also become a site for the latest on stem cell research particularly in the area of osteoarthritis.

Industry/Entity Type

Medical

Font styles to use
Sans Serif

Colors
ffffff

Requirements
Nice to have
• To give you an idea these are some sites I like
http://daptrine.com/
http://fennikstudio.tv/
http://norvalgate.com/
Should not have
• Pictures of doctors in white coats or old fit people smiling

```html
<!DOCTYPE html>
<html lang="en">
<head>
<meta charset="utf-8">
<title>Dr Tom Harlow — Sports and Exercise Medicine</title>
<link rel="stylesheet" href="https://fonts.googleapis.com/css2?family=Open+Sans:wght@300;400;600&family=Ubuntu:wght@300;400;500&display=swap">
<style>
  :root {
    --white: #ffffff;
    --green: #3aaa35;
    --lime: #8cc63f;
    --ink: #3a3a3a;
    --grey-text: #6b6b6b;
    --beige: #efebe4;
    --rule: #dcdcdc;
    --footer: #0b0b0b;
    --button: #5c5c5c;
    --caption: rgba(60, 70, 80, 0.78);
    --fb: #3b5998;
    --tw: #2a9fd8;
    --rss: #f26522;
    --yt: #d9232d;
  }
  * { box-sizing: border-box; margin: 0; padding: 0; }
  html, body { width: 833px; height: 1200px; overflow: hidden; background: var(--white); }
  body { position: relative; font-family: "Open Sans", Arial, sans-serif; color: var(--ink); }

  .site-header { position: absolute; top: 0; left: 0; width: 833px; height: 127px; }
  .brand { position: absolute; left: 60px; top: 20px; display: flex; flex-direction: column; align-items: flex-start; gap: 6px; }
  .brand-mark { width: 52px; height: 52px; border-radius: 50%; background: var(--lime); margin-left: 28px; }
  .brand-name { font-family: "Ubuntu", sans-serif; font-size: 20px; font-weight: 400; color: #2a3d7a; }
  .search { position: absolute; right: 60px; top: 33px; width: 181px; height: 25px; border: 1px solid #cfcfcf; display: flex; align-items: center; justify-content: space-between; padding: 0 8px; font-size: 10px; color: #888; }
  .main-nav { position: absolute; right: 60px; top: 82px; display: flex; gap: 23px; font-size: 12px; }
  .main-nav a { color: var(--ink); text-decoration: none; position: relative; padding: 0 4px 11px; }
  .main-nav a.active::after { content: ""; position: absolute; left: 0; right: 0; bottom: 0; height: 3px; background: var(--lime); }

  .hero { position: absolute; top: 127px; left: 0; width: 833px; height: 298px; background: linear-gradient(90deg, #6e8ea8 0%, #9bb4c7 45%, #c7d6e1 75%, #8fa8bb 100%); }
  .hero-arrow { position: absolute; top: 135px; }
  .hero-arrow.prev { left: 62px; }
  .hero-arrow.next { right: 62px; }
  .hero-caption { position: absolute; left: 127px; top: 219px; width: 450px; height: 43px; background: var(--caption); color: var(--white); font-weight: 300; font-size: 20px; line-height: 43px; padding-left: 12px; letter-spacing: -0.2px; }

  .intro { position: absolute; top: 425px; left: 0; width: 833px; height: 232px; background: var(--beige); text-align: center; }
  .intro h1 { margin-top: 40px; font-size: 18px; font-weight: 400; color: #555; letter-spacing: 0.3px; }
  .intro p { margin: 18px auto 0; width: 740px; font-size: 12.5px; line-height: 25px; color: #666; letter-spacing: 0.2px; }

  .features { position: absolute; top: 583px; left: 0; width: 833px; display: flex; justify-content: space-between; padding: 0 54px; }
  .feature { width: 220px; text-align: center; }
  .feature-photo { width: 136px; height: 136px; border-radius: 50%; border: 5px solid var(--white); margin: 0 auto; }
  .feature h2 { margin-top: 13px; font-size: 14.5px; font-weight: 400; color: var(--green); }
  .feature p { margin-top: 8px; font-size: 10px; line-height: 17.5px; color: #555; }
  .more-btn { display: inline-block; margin-top: 8px; width: 49px; height: 20px; line-height: 20px; background: linear-gradient(#7a7a7a, var(--button)); color: var(--white); font-size: 10px; border-radius: 2px; }

  .divider { position: absolute; top: 871px; left: 60px; width: 713px; height: 1px; background: var(--rule); }

  .section-title { position: absolute; top: 912px; font-size: 14.5px; font-weight: 400; color: var(--green); }
  .welcome-title { left: 60px; }
  .blog-title { left: 472px; }
  .blog-arrows { position: absolute; left: 748px; top: 913px; }

  .welcome-photo { position: absolute; left: 60px; top: 955px; width: 114px; height: 123px; background: linear-gradient(135deg, #5b8fd0, #a9ccef 55%, #c47a5a); }
  .welcome-text { position: absolute; left: 190px; top: 953px; width: 215px; font-family: "Ubuntu", sans-serif; font-weight: 300; font-size: 9.6px; line-height: 17.5px; color: #444; }
  .welcome-text .lead { text-transform: uppercase; margin-bottom: 5px; }

  .post-photo { position: absolute; left: 472px; top: 955px; width: 134px; height: 123px; background: radial-gradient(circle at 45% 45%, #3a5fb8, #0d1a4a 75%); }
  .post-date { position: absolute; left: 13px; top: 0; width: 36px; height: 42px; background: var(--lime); color: var(--white); text-align: center; font-family: "Ubuntu", sans-serif; }
  .post-date .day { display: block; font-size: 18px; line-height: 24px; }
  .post-date .month { display: block; font-size: 11px; }
  .post-text { position: absolute; left: 618px; top: 953px; width: 150px; font-family: "Ubuntu", sans-serif; font-size: 9.6px; line-height: 17.5px; color: #444; font-weight: 300; }
  .post-text h3 { font-size: 11px; font-weight: 500; color: #333; margin-bottom: 3px; }

  .site-footer { position: absolute; top: 1132px; left: 0; width: 833px; height: 68px; background: var(--footer); color: var(--white); font-family: "Ubuntu", sans-serif; font-size: 9.6px; }
  .footer-nav { position: absolute; left: 65px; top: 18px; }
  .copyright { position: absolute; left: 65px; top: 41px; }
  .social { position: absolute; left: 610px; top: 25px; display: flex; gap: 8px; }
  .social span { width: 26px; height: 26px; display: block; }
  .social .fb { background: var(--fb); }
  .social .tw { background: var(--tw); }
  .social .rss { background: var(--rss); }
  .social .yt { background: var(--yt); }
</style>
</head>
<body>
  <header class="site-header">
    <div class="brand">
      <span class="brand-mark"></span>
      <span class="brand-name">Dr Tom Harlow</span>
    </div>
    <div class="search">
      <span>Search..</span>
      <svg width="10" height="10" viewBox="0 0 10 10"><circle cx="4" cy="4" r="3" fill="none" stroke="#999" stroke-width="1.4"/><line x1="6.2" y1="6.2" x2="9" y2="9" stroke="#999" stroke-width="1.4"/></svg>
    </div>
    <nav class="main-nav">
      <a class="active" href="#">HOME</a>
      <a href="#">LOCATIONS</a>
      <a href="#">RESEARCH</a>
      <a href="#">SORT ME OUT</a>
      <a href="#">SOCIAL</a>
      <a href="#">BLOG</a>
      <a href="#">BIO</a>
    </nav>
  </header>

  <section class="hero" role="img" aria-label="Laboratory photo: a pipette dropping liquid into a glass beaker, in blue tones">
    <svg class="hero-arrow prev" width="28" height="56" viewBox="0 0 28 56"><polyline points="24,2 4,28 24,54" fill="none" stroke="#ffffff" stroke-opacity="0.7" stroke-width="1.5"/><line x1="20" y1="14" x2="20" y2="42" stroke="#ffffff" stroke-opacity="0.7" stroke-width="1.5"/></svg>
    <svg class="hero-arrow next" width="28" height="56" viewBox="0 0 28 56"><polyline points="4,2 24,28 4,54" fill="none" stroke="#ffffff" stroke-opacity="0.7" stroke-width="1.5"/><line x1="8" y1="14" x2="8" y2="42" stroke="#ffffff" stroke-opacity="0.7" stroke-width="1.5"/></svg>
    <div class="hero-caption">LOREM IPSUM DOLOR SIT AMET, CONSECTETUR</div>
  </section>

  <section class="intro">
    <h1>HENDRERIT IN VULPUTATE VELIT ESSE MOLESTIE CONSEQUAT</h1>
    <p>TYPI NON HABENT CLARITATEM INSITAM;ST USUS LEGENTIS IN IIS QUI FACIT EORUM CLARITATEM. INVESTIGATIONES DEMONSTRAVERUNT LECTORES LEGERE ME LIUS QUOD II LEGUNT SAEPIUS.</p>
  </section>

  <section class="features">
    <article class="feature">
      <div class="feature-photo" role="img" aria-label="Photo of a pipette over red liquid in lab dishes" style="background: radial-gradient(circle at 50% 55%, #d8204a, #f3a3b8 80%);"></div>
      <h2>RESEARCH</h2>
      <p>Vivamus vel eros eet mgna volutpat sagi tts. Nulla faucibus nibh a mgna tinciunt accu msan amet ante hndrerit</p>
      <span class="more-btn">MORE</span>
    </article>
    <article class="feature">
      <div class="feature-photo" role="img" aria-label="Photo of a gloved hand working with lab tubes" style="background: radial-gradient(circle at 40% 50%, #c9b15a, #6d6e5f 75%);"></div>
      <h2>SORT ME OUT</h2>
      <p>Vivamus vel eros eet mgna volutpat sagi tis. Nulla faucibus nibh a mgna tinciunt accu msan amet ante hndrerit</p>
      <span class="more-btn">MORE</span>
    </article>
    <article class="feature">
      <div class="feature-photo" role="img" aria-label="Microscope image of cells in cyan" style="background: radial-gradient(circle at 50% 50%, #3fc7d8, #0b7d94 80%);"></div>
      <h2>BIO</h2>
      <p>Vivamus vel eros eget magna volutpat sagi ttis. Nulla faucibus nibh a magna tincidunt accu msan amet ante hendrerit</p>
      <span class="more-btn">MORE</span>
    </article>
  </section>

  <div class="divider"></div>

  <h2 class="section-title welcome-title">WELCOME TO OUR WEBSITE!</h2>
  <div class="welcome-photo" role="img" aria-label="Photo of a hand holding test tubes in blue light"></div>
  <div class="welcome-text">
    <p class="lead">Mes cuml dia sed ineiinias ingoerto lot tes dolore ipsum. Mes cuml dia sed.</p>
    <p>Nemo enim ipsam voluptatem voluiptas Asp aut odit aut fugit sed quia consequuntur nid eos qui rationevoluptatem nesciunt lauenna lingerto otis aliiqt sit amet eism coeismod ict gulate ameti dapibus.</p>
  </div>

  <h2 class="section-title blog-title">BLOG POSTS</h2>
  <svg class="blog-arrows" width="26" height="14" viewBox="0 0 26 14"><polyline points="8,1 2,7 8,13" fill="none" stroke="#999" stroke-width="1.5"/><polyline points="18,1 24,7 18,13" fill="none" stroke="#999" stroke-width="1.5"/></svg>
  <div class="post-photo" role="img" aria-label="Illustration of glowing nerve cells on a dark blue background">
    <div class="post-date"><span class="day">8</span><span class="month">NOV</span></div>
  </div>
  <div class="post-text">
    <h3>Lorem ipsum dr sit amet</h3>
    <p>Nemo enim ipsam volm volu iptas sit. Asp aut odigit sedq uia consequuntur magniuirti on evoluptatem nescinusuen nalingerto otis aliiqt sit ame t eismcom. eismod ictgul.</p>
  </div>

  <footer class="site-footer">
    <div class="footer-nav">Home | Locations | Research | Sort me Out | Social | Blog | Bio</div>
    <div class="copyright">Copyrights 2013. All Rights Reserved.</div>
    <div class="social">
      <span class="fb"></span>
      <span class="tw"></span>
      <span class="rss"></span>
      <span class="yt"></span>
    </div>
  </footer>
</body>
</html>
```